Briskly Verdant Vessel Plots

We need a socialnook page designed that matches the logo on our business card (See separate brief on Pixel Forum). We are a small business that design compact succulent gardens using our imagination to pair the natural qualities of the plants with their containers. Wherever possible we carefully select upcycled, quirky, vintage and recycled materials for our containers so that each piece is unique. Succulents require very little maintenance and in Spring and Summer will delight and suprise you with their unexpected and sometimes quite spectacular display of flowers. We also offer a small range of delightful individually handcrafted garden art windchimes and mobiles also made from carefully selected vintage items.
Contact Information : Message Me @ SN or email Moira via Briskly.Verdant@fernpost.example to arrange pick up and address details in Wendmoor Brisbane.

(CAN YOU PLEASE DELETE ANY PICS WHICH ARE BADLY OUT OF FOCUS - I HAVE A LOT OF TROUBLE WITH MY DSLR CAMERA AS MY EYES ARE GETTING BAD)

I would like the Echinevera Lilac Rose as our Logo if possible but the photo came from imagevault and should be attributed somewhere to "lanternfox."

thanks Moira

This project has been bundled with a Business Card Design Project: http://jobs.pixelforum.example/job.aspx?id=517064

I encourage you to submit to both projects and keep designs consistent.

Target Market(s)

The target market is adults in South East Queensland aged 18 -75 looking for unusual and personalised gifts particularly for people who enjoy gardening or live in an apartment wth limited opportunity for gardening and those who appreciate vintage, quirky and upcycled things.

Industry/Entity Type

Small Business

Font styles to use
Script

Colors

Designer to choose colors to be used in the design.

Requirements
Must have

• I would like the Echinevera Lilac Rose as our Logo if possible but the photo came from imagevault and should be attributed somewhere to "lanternfox." This photo is in the bottom right hand corner.

The SN page must complement and be consistent with the "branding" on the business cards project.
Nice to have
• I quite like the script type of font but not too curly and feminine as this product has to appeal to men and women alike. So something a bit sophisticated but not "girly"

I quite like the second pic in the second row of the faces and curly tales and the first two shots in the bottom row should go on the SN page somewhere as a collection of current stock (though it is constantly growing - pardon the pun)
Should not have
• (CAN YOU PLEASE DELETE ANY PICS I have uploaded WHICH ARE BADLY OUT OF FOCUS - I HAVE A LOT OF TROUBLE WITH MY DSLR CAMERA AS MY EYES ARE GETTING BAD)

There are some minatures there which have been planted in corks and mounted on boards with stencil decorations - these obviously need to be turned around 90 degrees.

```html
<!DOCTYPE html>
<html lang="en">
<head>
<meta charset="utf-8">
<title>Briskly Verdant – socialnook page</title>
<link rel="stylesheet" href="https://fonts.googleapis.com/css2?family=Arimo:wght@400;700&display=swap">
<style>
:root{
  --page-bg:#e9eaed;
  --bar-top:#5a6ca6;
  --bar-bottom:#46589a;
  --bar-line:#35467f;
  --white:#ffffff;
  --ink:#1d2129;
  --ink-soft:#4b4f56;
  --ink-muted:#90949c;
  --link:#3b5998;
  --line:#dddfe2;
  --panel-head:#f6f7f9;
  --tab-accent:#4e69a2;
  --btn-bg:#f6f7f9;
  --btn-line:#ced0d4;
  --leaf-mid:#5f7a55;
  --leaf-light:#9bb08a;
  --stone:#a59a8a;
  --profile-top:#8fae6a;
  --profile-bottom:#4f6f8e;
}
*{box-sizing:border-box;margin:0;padding:0}
html,body{width:1200px;height:809px;overflow:hidden}
body{background:var(--page-bg);font-family:"Arimo",Helvetica,Arial,sans-serif;color:var(--ink);position:relative}
.abs{position:absolute}
.sr-only{position:absolute;width:1px;height:1px;overflow:hidden;clip:rect(0 0 0 0);white-space:nowrap}

/* top bar */
.top-bar{left:0;top:0;width:1200px;height:46px;background:linear-gradient(var(--bar-top),var(--bar-bottom));border-bottom:1px solid var(--bar-line)}
.brand-square{left:132px;top:12px;width:24px;height:24px;background:var(--white);border-radius:2px}
.search{left:164px;top:11px;width:618px;height:25px;background:var(--white);border:1px solid var(--bar-line);border-radius:2px;font-size:14px;line-height:23px;padding-left:12px;color:var(--ink)}
.search svg{position:absolute;right:7px;top:5px}
.user{left:850px;top:13px;display:flex;align-items:center;gap:6px;color:var(--white);font-weight:700;font-size:13px}
.user-avatar{width:20px;height:20px;background:linear-gradient(135deg,#c89a7a,#6b4d3c);border-radius:1px}
.nav-sep{top:13px;width:1px;height:20px;background:rgba(0,0,0,.2)}
.home{left:942px;top:15px;color:var(--white);font-weight:700;font-size:13px}
.top-icon{top:12px}

/* cover */
.cover{left:132px;top:56px;width:906px;height:336px;background:
  radial-gradient(ellipse at 45% 40%,var(--leaf-mid) 0%,transparent 45%),
  radial-gradient(ellipse at 85% 35%,var(--leaf-light) 0%,transparent 35%),
  radial-gradient(ellipse at 30% 85%,var(--stone) 0%,transparent 40%),
  linear-gradient(160deg,#4c5f45 0%,#3a4636 45%,#6e6a5e 80%,#2c2f2a 100%)}
.cover-shade{left:132px;top:240px;width:906px;height:152px;background:linear-gradient(transparent,rgba(0,0,0,.45))}
.profile-frame{left:161px;top:258px;width:151px;height:149px;background:var(--white);border:1px solid rgba(0,0,0,.15);border-radius:3px;padding:4px}
.profile-pic{width:100%;height:100%;background:linear-gradient(180deg,var(--profile-top),var(--profile-bottom))}
.page-name{left:343px;top:329px;color:var(--white);font-weight:700;font-size:26px;text-shadow:0 1px 3px rgba(0,0,0,.6)}
.page-type{left:343px;top:360px;color:var(--white);font-size:17px;text-shadow:0 1px 3px rgba(0,0,0,.6)}
.btn{top:350px;height:29px;background:var(--btn-bg);border:1px solid var(--btn-line);border-radius:2px;font-size:13px;font-weight:700;color:var(--ink-soft);display:flex;align-items:center;justify-content:center;gap:5px}
.btn-follow{color:#b0b3b8;font-weight:400}

/* tabs */
.tab-bar{left:132px;top:392px;width:906px;height:47px;background:var(--white);border:1px solid var(--line);border-top:none}
.tab{top:408px;font-size:15px;color:var(--ink-soft)}
.tab-active{color:var(--ink);font-weight:700}
.tab-underline{left:343px;top:434px;width:67px;height:4px;background:var(--tab-accent)}
.tab-sep{top:404px;width:1px;height:24px;background:var(--line)}

/* about */
.about{left:132px;top:450px;width:349px;height:152px;background:var(--white);border:1px solid var(--line);border-radius:2px}
.about-head{height:39px;background:var(--panel-head);border-bottom:1px solid var(--line);font-size:12px;font-weight:700;color:var(--ink-soft);padding:14px 0 0 12px;position:relative}
.about-head svg{position:absolute;right:12px;top:14px}
.about-row{position:absolute;left:12px;display:flex;align-items:center;gap:14px;font-size:15px}
.about-rule{position:absolute;left:12px;top:105px;width:324px;height:1px;background:var(--line)}

/* post */
.post{left:493px;top:450px;width:545px;height:310px;background:var(--white);border:1px solid var(--line);border-radius:2px}
.post-avatar{position:absolute;left:17px;top:18px;width:32px;height:32px;background:linear-gradient(180deg,var(--profile-top),var(--profile-bottom))}
.post-line{position:absolute;left:66px;top:19px;font-size:13px;color:var(--ink-soft)}
.post-line b,.post-line a{color:var(--link);text-decoration:none}
.post-time{position:absolute;left:66px;top:37px;font-size:12px;color:var(--ink-muted);display:flex;align-items:center;gap:3px}
.post-photo{position:absolute;left:4px;top:73px;width:537px;height:198px;background:
  radial-gradient(ellipse at 45% 45%,var(--leaf-mid) 0%,transparent 45%),
  radial-gradient(ellipse at 85% 30%,var(--leaf-light) 0%,transparent 35%),
  radial-gradient(ellipse at 25% 80%,var(--stone) 0%,transparent 40%),
  linear-gradient(160deg,#4c5f45 0%,#3a4636 45%,#6e6a5e 80%,#2c2f2a 100%)}
.post-actions{position:absolute;left:13px;top:284px;font-size:12px;color:var(--link)}
</style>
</head>
<body>

<header class="top-bar abs"></header>
<div class="brand-square abs"><span class="sr-only">socialnook</span></div>
<div class="search abs">BRISKLY VERDANT
  <svg width="14" height="14" viewBox="0 0 14 14"><circle cx="5.5" cy="5.5" r="4.2" fill="none" stroke="#4b4f56" stroke-width="1.8"/><line x1="8.6" y1="8.6" x2="12.8" y2="12.8" stroke="#4b4f56" stroke-width="2"/></svg>
</div>
<div class="user abs"><span class="user-avatar"></span>Callum</div>
<span class="nav-sep abs" style="left:933px"></span>
<div class="home abs">Home</div>
<svg class="top-icon abs" style="left:1010px" width="24" height="22" viewBox="0 0 24 22"><circle cx="9" cy="6" r="4" fill="#2e3e73"/><path d="M2 19c0-5 3-7 7-7s7 2 7 7z" fill="#2e3e73"/><circle cx="16" cy="6" r="3.5" fill="#2e3e73"/><path d="M15 12c4 0 7 2 7 7h-5" fill="#2e3e73"/></svg>
<svg class="top-icon abs" style="left:1044px" width="24" height="22" viewBox="0 0 24 22"><rect x="2" y="3" width="14" height="10" rx="1" fill="#2e3e73"/><path d="M4 13v5l4-5z" fill="#2e3e73"/><rect x="9" y="8" width="13" height="9" rx="1" fill="#2e3e73" stroke="#4f61a0"/></svg>
<svg class="top-icon abs" style="left:1077px" width="22" height="22" viewBox="0 0 22 22"><circle cx="11" cy="11" r="9" fill="#2e3e73"/><path d="M6 6c3 1 2 4 5 4s1 5 4 6" stroke="#4f61a0" stroke-width="2" fill="none"/></svg>
<span class="nav-sep abs" style="left:1118px"></span>
<svg class="top-icon abs" style="left:1130px" width="22" height="22" viewBox="0 0 22 22"><rect x="3" y="9" width="16" height="10" rx="1" fill="#2e3e73"/><path d="M6 9V6a5 5 0 0 1 10 0v3" stroke="#2e3e73" stroke-width="2.4" fill="none"/></svg>
<svg class="top-icon abs" style="left:1160px;top:19px" width="12" height="8" viewBox="0 0 12 8"><path d="M0 0h12L6 7z" fill="#2e3e73"/></svg>

<div class="cover abs" role="img" aria-label="Cover photo: close-up of green succulent rosettes among pebbles"></div>
<div class="cover-shade abs"></div>
<div class="profile-frame abs"><div class="profile-pic" role="img" aria-label="Profile photo: succulent in a blue pot"></div></div>
<div class="page-name abs">Briskly Verdant</div>
<div class="page-type abs">Local Business</div>

<div class="btn abs" style="left:733px;width:69px">
  <svg width="13" height="12" viewBox="0 0 13 12"><rect x="0" y="5" width="3" height="7" fill="#4b4f56"/><path d="M4 5l3-5c1.5 0 2 1 1.6 2.5L8 4.5h4c.8 0 1.2.8 1 1.5l-1.4 5c-.2.6-.6 1-1.2 1H4z" fill="#4b4f56"/></svg>Like</div>
<div class="btn btn-follow abs" style="left:809px;width:75px"><span style="font-size:16px">+</span>Follow</div>
<div class="btn abs" style="left:888px;width:90px">
  <svg width="12" height="12" viewBox="0 0 12 12"><path d="M0 0h12v8H5l-3 3V8H0z" fill="#4b4f56"/></svg>Message</div>
<div class="btn abs" style="left:982px;width:42px">
  <svg width="18" height="4" viewBox="0 0 18 4"><circle cx="2" cy="2" r="2" fill="#4b4f56"/><circle cx="9" cy="2" r="2" fill="#4b4f56"/><circle cx="16" cy="2" r="2" fill="#4b4f56"/></svg></div>

<nav class="tab-bar abs"></nav>
<span class="tab tab-active abs" style="left:343px">Timeline</span>
<span class="tab-underline abs"></span>
<span class="tab abs" style="left:442px">About</span>
<span class="tab-sep abs" style="left:502px"></span>
<span class="tab abs" style="left:517px">Welcome</span>
<span class="tab-sep abs" style="left:598px"></span>
<span class="tab abs" style="left:614px">SNW</span>
<span class="tab-sep abs" style="left:666px"></span>
<span class="tab abs" style="left:683px">More <svg width="9" height="6" viewBox="0 0 9 6"><path d="M0 0h9L4.5 5z" fill="#4b4f56"/></svg></span>

<section class="about abs">
  <div class="about-head">ABOUT
    <svg width="7" height="11" viewBox="0 0 7 11"><path d="M1 1l4.5 4.5L1 10" stroke="#90949c" stroke-width="2" fill="none"/></svg>
  </div>
  <div class="about-row" style="top:51px;color:var(--ink-soft)">
    <svg width="11" height="15" viewBox="0 0 11 15"><path d="M5.5 0A5.5 5.5 0 0 0 0 5.5C0 9.5 5.5 15 5.5 15S11 9.5 11 5.5A5.5 5.5 0 0 0 5.5 0z" fill="#7f838a"/><circle cx="5.5" cy="5.5" r="2" fill="#fff"/></svg>
    Brisbane, Queensland, Australia</div>
  <div class="about-rule"></div>
  <div class="about-row" style="top:118px;gap:10px">
    <svg width="12" height="12" viewBox="0 0 12 12"><path d="M2.5 0L5 3 3.6 4.6c.8 1.6 2.2 3 3.8 3.8L9 7l3 2.5L10.2 12C4.6 11.5.5 7.4 0 1.8z" fill="#7f838a"/></svg>
    +VERY Long Distance</div>
</section>

<article class="post abs">
  <div class="post-avatar" role="img" aria-label="Page avatar: succulent in a blue pot"></div>
  <div class="post-line"><b>Briskly Verdant</b> changed their <a>cover photo</a>.</div>
  <div class="post-time">3 minutes ago
    <svg width="10" height="10" viewBox="0 0 10 10"><circle cx="5" cy="5" r="4.5" fill="#90949c"/><path d="M2.5 3c1.5.5 1 2 2.5 2s.5 2.5 2 3" stroke="#fff" fill="none"/></svg></div>
  <div class="post-photo" role="img" aria-label="New cover photo: close-up of green succulent rosettes among pebbles"></div>
  <div class="post-actions">Like · Comment · Share</div>
</article>

</body>
</html>
```